FlockVault.net website design

We are looking for a design for a new website we are about to launch called FlockVault.net. FlockVault.net is an online discount wine site that will focus on selling only one wine at a time. (This potentially may become two or three wines at a time in the future but only one for now). The wine that is up for sale will not actually be sold until a pre-set number of buyers “the group” commits to buying the wine. If the threshold of buyers is not met then the wine is not sold. This group aspect is what makes the site unique. By only selling the wine when the group commits to buying it we are able to deliver them a great wine at a fantastic price.
The website should convey a fun feeling while also indicating that this is a place where serious wine enthusiasts can shop. We will be providing information, ratings, and reviews about the wines that are currently on sale.
Updates
Target Market(s)
The target market is a wide range of wine enthusiasts, from people in their 20s and 30s to more mature and serious wine connoisseurs.
Industry/Entity Type
Shop
Requirements
Must have
- Below is a list of specifications for the website:
1) Main page with our logo (which includes green, purple, and a magenta wine color) that showcases the current wine that's for sale
- The site’s main focus should be on selling ONE bottle of wine at a time at group rate.
- The site should capture the group buying concept as this is what differentiates our site from the others. Visitors to the site should get the sense that they are part of a special community that is getting a great deal because they are buying the wine as a group.
- A meter or better yet an animation should be used to indicate if the tipping point has been met for a sale. We’d like to see some creative ideas here.
- Nice high-res photo of the wine bottle
- Detailed description of what kind of wine it is, where the wine is from, type of grape, vino observer and other ratings, description of what it tastes like. We would like the option to provide as much detail here as possible.
- Breakdown on what the prices are per bottle and the discount we're giving. We would like to show the original price as compared to the FlockVault.net price.
- Potentially show a list of upcoming wines. Maybe not the exact wine that will be for sale next but some info to entice users to keep checking.
2) User Account Log in
- Ability to create and log into a personal account
The personal account should be able to:
-store users' credit card and shipping information as well as past orders
-allow you to opt in or out of flock vault emails
-potentially store wine preference or ratings information
-refer a friend option where you get some kind of incentive
3) The Group Concept. The website design must include a few aspects that identify FlockVault.net as a social site, not simply a wine sale site.
- Some kind of indicator showing if the group threshold has been met or not. We would like to see some type of animation with wine bottles filling up, or grapes on a scale-something that would change as the number of people buying into the sale increase.
- Button to join the group purchase
4) General Site Content must include:
- Email link to send questions to support
- Information on how shipping works and other FAQs
- Legal disclaimer
- Links to Friendbook and Chirper
Nice to have
- It would be nice to have a discussion board where FlockVault members can discuss wines.
Should not have
- The design should not be for a general wine store that sells a variety of different wines.

```html
<!DOCTYPE html>
<html lang="en">
<head>
<meta charset="utf-8">
<title>FlockVault – FAQs</title>
<link rel="stylesheet" href="https://fonts.googleapis.com/css2?family=Alfa+Slab+One&family=Lora:wght@600;700&family=Open+Sans:wght@400;600&family=Nunito:wght@700;800&display=swap">
<style>
:root{
  --plum-deep:#2e1426;
  --plum:#4f2442;
  --plum-glow:#6a3158;
  --nav-top:#b552c4;
  --nav-bottom:#7a1f8a;
  --nav-text:#3a0a3a;
  --magenta:#a83565;
  --magenta-btn:#b23a6a;
  --purple-q:#8c2f90;
  --green:#8cc63f;
  --violet:#b03ac0;
  --sand:#efebe4;
  --tab:#cfc9c0;
  --wood-a:#d9c4a0;
  --wood-b:#c7ad86;
  --ink:#222;
  --rule:#e4e0da;
  --white:#fff;
}
*{box-sizing:border-box;margin:0;padding:0}
html,body{width:1200px;height:1164px;overflow:hidden}
body{position:relative;font-family:"Open Sans",sans-serif;color:var(--ink);
  background:radial-gradient(ellipse 700px 260px at 600px 320px,var(--plum-glow),transparent 70%),
  linear-gradient(var(--plum-deep),var(--plum) 60%,var(--plum-deep));}
.floor{position:absolute;left:0;top:888px;width:1200px;height:276px;
  background:linear-gradient(90deg,var(--wood-a),var(--wood-b),var(--wood-a),var(--wood-b),var(--wood-a));}
.brand{position:absolute;left:36px;top:34px;display:flex;align-items:center;gap:14px}
.brand-dot{width:70px;height:70px;border-radius:50%;background:var(--violet)}
.brand-name{font-family:"Nunito",sans-serif;font-weight:800;font-size:50px;color:var(--green);line-height:1}
.nav{position:absolute;left:24px;top:142px;width:1152px;height:66px;border-radius:8px;
  background:linear-gradient(var(--nav-top),var(--nav-bottom));box-shadow:0 2px 4px rgba(0,0,0,.5);
  display:flex;align-items:center;padding-left:14px;font-family:"Lora",serif;font-weight:700;font-size:24px}
.nav a{color:var(--nav-text);text-decoration:none;margin-right:40px}
.nav .active{background:linear-gradient(#f4ebe6,#c9b7b0);border-radius:6px;padding:8px 13px;margin-right:28px;color:#1d0c18}
.cart{position:absolute;right:22px;top:18px;display:flex;align-items:center;gap:8px;color:#fff;font-size:21px;font-weight:600;font-family:"Lora",serif}
.banner{position:absolute;left:26px;top:234px}
.main{position:absolute;left:24px;top:358px;width:1152px;height:640px;background:var(--sand);border-radius:8px}
.faq{position:absolute;left:6px;top:6px;width:854px;height:628px;background:var(--white);
  box-shadow:2px 0 4px rgba(0,0,0,.25);padding:24px 24px 0 24px}
.faq h1{font-size:34px;font-weight:600;color:var(--magenta);margin:0 0 14px 8px}
.item{border-bottom:1px solid var(--rule);padding:10px 0 12px}
.q,.a{display:flex}
.q{font-size:15.5px;line-height:21.5px;color:var(--purple-q);margin-bottom:6px}
.q b{font-family:"Lora",serif;width:28px;flex:none;padding-left:2px}
.a{font-size:12.4px;line-height:21.6px;color:var(--ink)}
.a b{width:28px;flex:none;padding-left:2px;font-size:12px}
.tab{position:absolute;left:860px;width:180px;height:44px;background:var(--tab);border-radius:0 6px 6px 0;
  font-size:18px;color:#5b5450;padding:10px 0 0 24px}
.field{position:absolute;left:884px;width:240px;height:36px;background:#fff;border:1px solid #cfcac3;border-radius:6px;
  font-size:13px;color:#777;padding:8px 12px}
.btn{position:absolute;background:var(--magenta-btn);color:#fff;border-radius:5px;font-size:15px;text-align:center;line-height:34px}
.side-text{position:absolute;font-size:13px}
.forgot{left:990px;top:190px;color:#a01e4e;font-size:12px}
.free{left:1031px;top:297px;font-size:21px;color:var(--magenta)}
.age{left:888px;top:340px;font-size:12px}
.boards{position:absolute;left:868px;top:541px;width:280px;height:93px;background:#d7d0ca;border-radius:6px}
.boards-label{position:absolute;left:78px;top:22px;font-family:"Nunito",sans-serif;font-weight:800;color:#2a0f1e;line-height:24px}
.footer{position:absolute;left:24px;top:1051px;width:1152px;height:87px;background:#fff;border-radius:6px}
.subscribe{position:absolute;left:2px;top:4px;width:510px;height:79px;border:1px solid #ddd;border-radius:4px}
.subscribe h2{position:absolute;left:8px;top:8px;font-size:22px;font-weight:700;color:#a01e4e}
.subscribe p{position:absolute;left:10px;top:46px;font-size:12.5px}
.email{position:absolute;left:238px;top:35px;width:226px;height:34px;background:#e2dbd6;font-size:12.5px;padding:8px 10px;color:#333}
.go{position:absolute;left:464px;top:35px;width:36px;height:34px;background:#a01e4e}
.social{position:absolute;right:14px;top:12px;display:flex;align-items:center;gap:6px;font-size:13px}
.social i{display:inline-block;width:24px;height:24px;border-radius:50%;margin-left:6px}
.copy{position:absolute;right:14px;top:58px;font-size:12px}
</style>
</head>
<body>
<div class="floor" role="img" aria-label="Light wooden floor texture"></div>

<div class="brand"><span class="brand-dot"></span><span class="brand-name">FlockVault</span></div>

<nav class="nav">
  <a class="active">Home</a><a>About</a><a>How it Works</a><a>FAQs</a><a>Support</a><a>Contact Us</a>
  <div class="cart">
    <svg width="28" height="24" viewBox="0 0 28 24"><path d="M1 2h5l3 13h14l3-9H8" fill="none" stroke="#2a0a24" stroke-width="2.5"/><circle cx="11" cy="20" r="2.5" fill="#2a0a24"/><circle cx="21" cy="20" r="2.5" fill="#2a0a24"/></svg>
    <span>Cart 0 items</span>
  </div>
</nav>

<svg class="banner" width="1148" height="92" viewBox="0 0 1148 92">
  <path d="M14 2H1134l12 14v60l-12 14H14L2 76V16z" fill="#4a2040" stroke="#7a4a6a" stroke-width="2"/>
  <text x="32" y="60" textLength="1085" lengthAdjust="spacingAndGlyphs" font-family="Alfa Slab One, serif" font-size="36" fill="#e8e4e8">SELLING <tspan fill="#8cc63f">ONE BOTTLE</tspan> OF WINE AT A TIME <tspan fill="#b03ac0">AT A GROUP RATE</tspan></text>
</svg>

<section class="main">
  <div class="faq">
    <h1>FAQs</h1>
    <div class="item"><div class="q"><b>Q:</b><span>Lorem ipsum dolor sit amet, consectetur adipisicing elit, sed do eiusmod tempor incididunt ut labore et dolore magna aliqua. Ut enim ad minim veniam</span></div>
      <div class="a"><b>A:</b><span>Lorem ipsum dolor sit amet, consectetur adipisicing elit, sed do eiusmod tempor incididunt ut labore et dolore magna aliqua. Ut enim ad minim veniam, quis nostrud exercitation ullamco laboris nisi ut aliquip ex ea commodo consequat. Duis aute irure dolor in reprehenderit in voluptate velit esse cillum dolore eu fugiat nulla pariatur. Excepteur sint occaecat cupidatat non proident, sunt in culpa qui officia deserunt mollit anim id est laborum.</span></div></div>
    <div class="item"><div class="q"><b>Q:</b><span>Lorem ipsum dolor sit amet, consectetur adipisicing elit, sed do eiusmod tempor incididunt ut labore et dolore magna aliqua. Ut enim ad minim veniam</span></div>
      <div class="a"><b>A:</b><span>Lorem ipsum dolor sit amet, consectetur adipisicing elit, sed do eiusmod tempor incididunt ut labore et dolore magna aliqua. Ut enim ad minim veniam, quis nostrud exercitation ullamco laboris nisi ut aliquip ex ea commodo consequat. Duis aute irure dolor in reprehenderit in voluptate velit esse cillum dolore eu fugiat nulla pariatur. Excepteur sint occaecat cupidatat non proident, sunt in culpa qui officia deserunt mollit anim id est laborum.</span></div></div>
    <div class="item"><div class="q"><b>Q:</b><span>Lorem ipsum dolor sit amet, consectetur adipisicing elit, sed do eiusmod tempor incididunt ut labore et dolore magna aliqua. Ut enim ad minim veniam</span></div>
      <div class="a"><b>A:</b><span>Lorem ipsum dolor sit amet, consectetur adipisicing elit, sed do eiusmod tempor incididunt ut labore et dolore magna aliqua. Ut enim ad minim veniam, quis nostrud exercitation ullamco laboris nisi ut aliquip ex ea commodo consequat. Duis aute irure dolor in reprehenderit in voluptate velit esse cillum dolore eu fugiat nulla pariatur. Excepteur sint occaecat cupidatat non proident, sunt in culpa qui officia deserunt mollit anim id est laborum.</span></div></div>
  </div>

  <div class="tab" style="top:18px">Member Sign In</div>
  <div class="field" style="top:82px">Email Address</div>
  <div class="field" style="top:132px">Password</div>
  <div class="btn" style="left:884px;top:182px;width:96px">SIGN IN</div>
  <div class="side-text forgot">Forgot Password?</div>
  <div class="tab" style="top:235px">Not A Member?</div>
  <div class="btn" style="left:884px;top:295px;width:135px">SIGN UP NOW!</div>
  <div class="side-text free">It's Free!</div>
  <div class="side-text age">Members must be 21 years or older</div>

  <div class="boards">
    <svg style="position:absolute;left:16px;top:22px" width="54" height="50" viewBox="0 0 54 50">
      <path d="M2 4h32v22H14l-8 8v-8H2z" fill="#f3b51c" stroke="#8a6a10"/>
      <path d="M18 18h34v22h-6v8l-8-8H18z" fill="#6fbf3a" stroke="#3d7a1a"/>
    </svg>
    <div class="boards-label"><span style="font-size:25px">DISCUSSION</span><br><span style="font-size:34px;line-height:32px">BOARDS</span></div>
    <svg style="position:absolute;left:244px;top:20px" width="24" height="56" viewBox="0 0 24 56"><path d="M3 2l18 26L3 54" fill="none" stroke="#4a2a3a" stroke-width="3"/></svg>
  </div>
</section>

<footer class="footer">
  <div class="subscribe">
    <h2>SUBSCRIBE</h2>
    <p>To receive special offers &amp; Promotions</p>
    <div class="email">Please Enter Your Email Address</div>
    <div class="go"><svg width="36" height="34" viewBox="0 0 36 34"><path d="M14 17h8m-3-3l3 3-3 3" stroke="#fff" fill="none"/></svg></div>
  </div>
  <div class="social">Find us on <i style="background:#3b5998"></i>Friendbook <i style="background:#3fa9e0"></i>Chirper</div>
  <div class="copy">© 2010 Flock Vault. All Rights Reserved.</div>
</footer>
</body>
</html>
```